Using attached logo that has been created

Business card with logo that's attached. Maybe with water or the cartoon van in background. Looking for it to not be so plain and not too white.
Information to include;
Dario Whitlock
(555) 208-7713
Info@mossbrookpipeworks.example
www.mossbrookpipeworks.example
License # 5320417
Looking forward to the designs u come up with.
Thank you!
-Teresa
The designer (Brynn), that I would like to work with requested an extension to allow time to create a couple designs for this project.
Target Market(s)
Plumbing
Industry/Entity Type
Plumbing
Contact Information for Business Card
Listed above
Font styles to use
Look and feel

```html
<!DOCTYPE html>
<html lang="en">
<head>
<meta charset="utf-8">
<title>Mossbrook Pipeworks – Business Card</title>
<link rel="stylesheet" href="https://fonts.googleapis.com/css2?family=Roboto+Slab:wght@400;700&display=swap">
<style>
  :root {
    --stage: #d9d4cc;
    --frost-top: #eef0f1;
    --frost-bottom: #d8d6d2;
    --gold: #e39a1c;
    --gold-dark: #a8650a;
    --ink-light: #e6e4df;
    --ink-soft: #cfd5e6;
    --brand-navy: #12307d;
    --placeholder: #c9ced8;
  }
  * { margin: 0; padding: 0; box-sizing: border-box; }
  html, body { width: 1200px; height: 969px; overflow: hidden; }
  body {
    background: var(--stage);
    font-family: "Roboto Slab", serif;
    position: relative;
  }
  .business-card {
    position: absolute;
    left: 80px; top: 188px;
    width: 1040px; height: 592px;
    border-radius: 24px;
    overflow: hidden;
    background: linear-gradient(180deg, var(--frost-top), var(--frost-bottom));
    box-shadow: 0 12px 36px rgba(0,0,0,.18);
  }
  .card-shapes { position: absolute; inset: 0; }
  .portrait-watermark {
    position: absolute;
    left: 40px; top: 40px;
    width: 330px; height: 300px;
    border-radius: 12px;
    background: rgba(80,110,190,.18);
  }
  .contact-block {
    position: absolute;
    left: 53px; top: 352px;
    color: var(--ink-light);
  }
  .contact-block .person-name {
    font-weight: 700;
    font-size: 31px;
    letter-spacing: 1px;
    text-transform: uppercase;
    margin-bottom: 24px;
  }
  .contact-block .license {
    font-size: 20px;
    margin-bottom: 20px;
  }
  .contact-list { list-style: none; }
  .contact-list li {
    display: flex; align-items: center;
    font-size: 19px;
    height: 30px;
    color: var(--ink-soft);
  }
  .contact-list svg { width: 18px; height: 18px; margin-right: 14px; flex: none; fill: var(--ink-light); }
  .mascot-area {
    position: absolute;
    left: 690px; top: 62px;
    width: 240px; height: 232px;
    border-radius: 12px;
    background: var(--placeholder);
  }
  .brand-name {
    position: absolute;
    left: 610px; top: 318px;
    width: 400px;
    text-align: center;
    font-weight: 700;
    font-size: 32px;
    line-height: 1.2;
    color: var(--brand-navy);
    letter-spacing: .5px;
  }
</style>
</head>
<body>
  <section class="business-card">
    <svg class="card-shapes" viewBox="0 0 1040 592" width="1040" height="592" aria-hidden="true">
      <defs>
        <linearGradient id="blueField" x1="0" y1="0" x2="1" y2="1">
          <stop offset="0" stop-color="#1e44a6"/>
          <stop offset=".55" stop-color="#163a93"/>
          <stop offset="1" stop-color="#081a4f"/>
        </linearGradient>
      </defs>
      <path d="M0,0 H303 C380,250 600,560 929,592 H0 Z" fill="url(#blueField)"/>
      <path d="M303,0 C380,250 600,560 929,592" fill="none" stroke="#061340" stroke-width="3"/>
      <path d="M312,6 C392,252 610,552 960,590" fill="none" stroke="var(--gold)" stroke-width="7" stroke-linecap="round"/>
      <path d="M316,10 C396,256 614,556 960,592" fill="none" stroke="var(--gold-dark)" stroke-width="2"/>
    </svg>

    <div class="portrait-watermark" role="img" aria-label="Faint illustration of the plumber mascot"></div>

    <div class="contact-block">
      <h1 class="person-name">Dario Whitlock</h1>
      <p class="license">License # 5320417</p>
      <ul class="contact-list">
        <li>
          <svg viewBox="0 0 24 24"><path d="M6.6 10.8a15.1 15.1 0 0 0 6.6 6.6l2.2-2.2c.3-.3.7-.4 1-.2 1.1.4 2.3.6 3.6.6.6 0 1 .4 1 1V20c0 .6-.4 1-1 1A17 17 0 0 1 3 4c0-.6.4-1 1-1h3.5c.6 0 1 .4 1 1 0 1.3.2 2.5.6 3.6.1.3 0 .7-.2 1z"/></svg>
          (555) 208-7713
        </li>
        <li>
          <svg viewBox="0 0 24 24"><path d="M2 5h20v14H2z M2 5l10 8 10-8" fill="none" stroke="#e6e4df" stroke-width="2"/></svg>
          Info@mossbrookpipeworks.example
        </li>
        <li>
          <svg viewBox="0 0 24 24"><circle cx="12" cy="12" r="9" fill="none" stroke="#e6e4df" stroke-width="2"/><path d="M3 12h18M12 3c3 3 3 15 0 18M12 3c-3 3-3 15 0 18" fill="none" stroke="#e6e4df" stroke-width="1.5"/></svg>
          www.mossbrookpipeworks.example
        </li>
      </ul>
    </div>

    <div class="mascot-area" role="img" aria-label="Mascot illustration of the plumber with tools"></div>
    <p class="brand-name">Mossbrook Pipeworks</p>
  </section>
</body>
</html>
```